Opportunity flyer for veterinarians about a partnering with LumaVet

We need a bifold or trifold flyer designed for veterinarians about offering In Home Pet Euthanasia in their area (across the nation). I have a rough template drafted but need an overall graphic designer with an eye to the need for a compassionate, peaceful, attractive and soft design fitting for this industry. The colors should be in the soft blues and lavender spectrum. I like water colors, soft lines and blurred effects. The flyer should communicate the benefits of offering this service to pet owners as well as the benefit to the vet: freedom, more income, flexibility and a solution to the burnout they often feel in their regular line of work. Not required to use the photos in the flyer

```html
<!DOCTYPE html>
<html lang="en">
<head>
<meta charset="utf-8">
<title>LumaVet Flyer</title>
<link rel="stylesheet" href="https://fonts.googleapis.com/css2?family=Poppins:ital,wght@0,400;0,500;0,600;0,700;1,600;1,700&display=swap">
<style>
  :root {
    --blue: #4f79b0;
    --blue-dark: #3f689f;
    --white: #ffffff;
    --ink: #111111;
    --backdrop: #e9e9e9;
    --paper: #ffffff;
  }
  * { box-sizing: border-box; margin: 0; padding: 0; }
  html, body { width: 1000px; height: 1200px; overflow: hidden; }
  body { background: var(--backdrop); font-family: "Poppins", sans-serif; position: relative; }

  .page {
    position: absolute; left: 119px; width: 731px; height: 516px;
    background: var(--paper); overflow: hidden;
    transform: scale(1.041); transform-origin: 0 0;
  }
  .page--outside { top: 43px; }
  .page--inside { top: 609px; }
  .page__shapes { position: absolute; inset: 0; width: 731px; height: 516px; }
  .text { position: absolute; }

  /* Outside page */
  .brand { left: 463px; top: 30px; color: var(--blue); }
  .brand__name { display: flex; align-items: center; gap: 8px; font-size: 30px; font-weight: 600; line-height: 1; }
  .brand__dot { width: 18px; height: 18px; border-radius: 50%; background: var(--blue); }
  .brand__tagline { margin-top: 6px; font-size: 12.5px; font-style: italic; font-weight: 600; }

  .vet-question { left: 472px; top: 316px; color: var(--white); font-size: 20px; font-weight: 700; font-style: italic; text-shadow: 0 1px 4px rgba(0,0,0,.35); }
  .vet-list { left: 385px; top: 383px; color: var(--white); font-size: 13px; line-height: 1.35; list-style: none; }
  .vet-list li { margin-bottom: 8px; }
  .vet-list li:nth-child(3) { margin-bottom: 2px; }

  .contact-intro { right: 390px; top: 360px; width: 320px; color: var(--white); font-size: 11px; line-height: 1.45; text-align: right; }
  .contact-intro strong { font-size: 16px; font-weight: 700; }
  .contact-line { right: 390px; color: var(--white); font-size: 13px; display: flex; align-items: center; gap: 6px; }
  .contact-line--email { top: 441px; }
  .contact-line--phone { top: 465px; }
  .contact-line svg { width: 12px; height: 12px; fill: var(--white); }

  /* Inside page */
  .mission-title { left: 22px; top: 30px; color: var(--white); font-size: 17px; font-weight: 700; line-height: 1.2; }
  .mission-body { left: 22px; top: 82px; width: 345px; color: var(--white); font-size: 7.8px; line-height: 1.42; }
  .mission-body p + p { margin-top: 8px; }

  .care-title { right: 36px; top: 64px; color: var(--ink); font-size: 16px; font-weight: 700; line-height: 1.35; text-align: right; }
  .care-body { right: 36px; top: 118px; width: 262px; color: var(--ink); font-size: 8px; line-height: 1.35; text-align: right; }

  .team-title { left: 22px; top: 290px; color: var(--ink); font-size: 16px; font-weight: 700; line-height: 1.3; }
  .team-list { left: 22px; top: 351px; font-size: 8.5px; color: var(--ink); list-style: none; }
  .team-list li { position: relative; padding-left: 12px; height: 17.3px; }
  .team-list li::before { content: ""; position: absolute; left: 0; top: 4px; width: 5px; height: 5px; border-radius: 50%; background: var(--ink); }

  .services { right: 41px; top: 410px; color: var(--white); font-size: 13px; font-weight: 700; line-height: 1.3; text-align: right; list-style: none; }
</style>
</head>
<body>

<section class="page page--outside">
  <svg class="page__shapes" viewBox="0 0 731 516">
    <defs>
      <linearGradient id="mono-photo" x1="0" y1="0" x2="1" y2="1">
        <stop offset="0" stop-color="#2b2b2b"/><stop offset=".5" stop-color="#6f6f6f"/><stop offset="1" stop-color="#cfcfcf"/>
      </linearGradient>
      <linearGradient id="pets-photo" x1="0" y1="0" x2="1" y2="1">
        <stop offset="0" stop-color="#f4f2ef"/><stop offset=".6" stop-color="#e6ddd3"/><stop offset="1" stop-color="#b58a62"/>
      </linearGradient>
    </defs>
    <path d="M0,280 C120,262 290,270 372,300 C380,380 365,460 335,516 L0,516 Z" fill="var(--blue)"/>
    <path d="M375,516 C360,400 420,250 520,150 C600,90 700,115 731,190 L731,516 Z" fill="var(--blue)"/>
    <ellipse cx="212" cy="150" rx="232" ry="168" transform="rotate(-22 212 150)" fill="url(#mono-photo)" stroke="var(--white)" stroke-width="4" role="img" aria-label="Black and white photo of a woman touching noses with a white Labrador"/>
    <ellipse cx="548" cy="235" rx="140" ry="128" fill="url(#pets-photo)" stroke="var(--white)" stroke-width="4" role="img" aria-label="Photo of a kitten and a puppy sleeping together on a soft blanket"/>
  </svg>

  <div class="text brand">
    <div class="brand__name"><span class="brand__dot"></span>LumaVet</div>
    <div class="brand__tagline">A Peaceful Passing At Home</div>
  </div>

  <div class="text vet-question">Are you a vet who...</div>
  <ul class="text vet-list">
    <li>Wants more Flexibility?</li>
    <li>Wants to offer IHE, but<br>don't know how to get started?</li>
    <li>Doesn't like answering phones or scheduling?</li>
    <li>Wants more Independence?</li>
  </ul>

  <p class="text contact-intro">We try to help all animals and will try to find a veterinarian that can help your particular pet. Please tell us a bit more about your pet and situation. You may alternatively call us at <strong>1-833-555-0147</strong></p>
  <div class="text contact-line contact-line--email">info@lumavet.example
    <svg viewBox="0 0 24 24"><path d="M2 5h20v14H2z M2 5l10 8 10-8" fill="none" stroke="#fff" stroke-width="2"/></svg>
  </div>
  <div class="text contact-line contact-line--phone">(833) 555 - 0147
    <svg viewBox="0 0 24 24"><path d="M6.6 10.8a15 15 0 006.6 6.6l2.2-2.2c.3-.3.7-.4 1-.2 1.1.4 2.3.6 3.6.6.6 0 1 .4 1 1V20c0 .6-.4 1-1 1C10.6 21 3 13.4 3 4c0-.6.4-1 1-1h3.5c.6 0 1 .4 1 1 0 1.3.2 2.5.6 3.6.1.3 0 .7-.2 1z"/></svg>
  </div>
</section>

<section class="page page--inside">
  <svg class="page__shapes" viewBox="0 0 731 516">
    <defs>
      <linearGradient id="hug-photo" x1="0" y1="0" x2="1" y2="1">
        <stop offset="0" stop-color="#3a2a22"/><stop offset=".45" stop-color="#7a2f35"/><stop offset=".75" stop-color="#b07a3e"/><stop offset="1" stop-color="#5c6b44"/>
      </linearGradient>
    </defs>
    <path d="M0,0 L352,0 C440,40 495,135 455,185 C415,232 300,238 200,232 C120,228 50,220 0,212 Z" fill="var(--blue)"/>
    <path d="M400,516 C368,420 400,250 482,212 C562,174 682,190 731,232 L731,516 Z" fill="var(--blue)"/>
    <ellipse cx="330" cy="345" rx="137" ry="130" fill="url(#hug-photo)" stroke="var(--white)" stroke-width="4" role="img" aria-label="Photo of a man hugging a happy golden retriever"/>

    <g class="service-icons" fill="var(--white)">
      <circle cx="532" cy="260" r="32"/>
      <circle cx="612" cy="272" r="32"/>
      <circle cx="543" cy="343" r="32"/>
      <circle cx="624" cy="348" r="32"/>
    </g>
    <g fill="none" stroke="var(--blue)" stroke-width="2.4" stroke-linejoin="round" stroke-linecap="round">
      <path d="M518,262 L532,248 L546,262 M521,259 L521,275 L543,275 L543,259"/>
      <path d="M606,262 L616,270 L610,280 M616,270 L622,278 M612,272 L604,272 M616,268 L624,266"/>
      <path d="M526,350 L536,350 L548,356 L560,350 M526,350 L526,358 L544,362 L562,354"/>
    </g>
    <g fill="var(--blue)">
      <circle cx="616" cy="258" r="3.5"/>
      <path d="M532,268 c-3,-3 -6,-2 -6,1 c0,3 6,6 6,6 c0,0 6,-3 6,-6 c0,-3 -3,-4 -6,-1z"/>
      <path d="M546,342 c-4,-5 -10,-3 -10,1 c0,5 10,9 10,9 c0,0 10,-4 10,-9 c0,-4 -6,-6 -10,-1z"/>
      <ellipse cx="624" cy="356" rx="9" ry="7"/>
      <circle cx="613" cy="344" r="3.5"/><circle cx="620" cy="338" r="3.5"/><circle cx="628" cy="338" r="3.5"/><circle cx="635" cy="344" r="3.5"/>
    </g>
  </svg>

  <h2 class="text mission-title">We strive to bring peace to<br>all pets and their families.</h2>
  <div class="text mission-body">
    <p>Our pets are more than just animals, they are our companions, our support, and our family. They bring joy, compassion, and love into our lives, leaving a lasting impression on our hearts. Luma, meaning "light" in Latin, refers to the gentle glow that remains at the close of a day. At LumaVet, we believe that the connection we form with our pets is much like that glow, an extension of something already complete in and of itself.</p>
    <p>LumaVet is dedicated to honoring that bond by celebrating the lives of the pets we cherish and providing resources, support, and love as they approach the end of their lives. We want to help them pass away peacefully, surrounded by the love and care they deserve.</p>
  </div>

  <h2 class="text care-title">Mobile end of life care for<br>your beloved pet</h2>
  <p class="text care-body">We are committed to helping you provide a peaceful passing for your pet in the comfort of your own home. From last goodbyes to aftercare you can find a local vet to bring peace for your pet and your family.</p>

  <h2 class="text team-title">Your LumaVet<br>Team Handles</h2>
  <ul class="text team-list">
    <li>Client Communication 24/7</li>
    <li>Collecting payments</li>
    <li>Books clients on Your schedule</li>
    <li>Markets Your IHE services &amp; pricing</li>
    <li>Handles Your Reviews</li>
    <li>Notifies rDVM of euthanasia</li>
    <li>Prepares Clients for appointment</li>
    <li>More!</li>
  </ul>

  <ul class="text services">
    <li>In-Home Euthanasia</li>
    <li>Aftercare &amp; Cremation</li>
    <li>Deceased Pet Pick Up</li>
    <li>Memorabilia</li>
  </ul>
</section>

</body>
</html>
```